Consulting firm needs a professional letterhead design

We need a professional letterhead design which is simple but unique. It should carry attributes of the latest designs in the market suitable for professional environmental consultancies.

- The logo is attached for you to USE.
- Our preferred color scheme is that shown in the logo.
- Letterhead text color is your choice to make.
- Logo to the left and text to the right plus slogan/tagline is desirable for this letterhead.

Use any address etc. of your choice in the letterhead.

Target Market(s)

Consulting firms and government agencies

Industry/Entity Type

Environmental Consultant

Colors
acd037
fece3e
85cae6
3277b5

Requirements
Must have
• Logo supplied and color scheme must be used.
Nice to have
• Nexa font is used in the Logo, so it would ne nice to have nexa font in the letterhead too.

```html
<!DOCTYPE html>
<html lang="en">
<head>
<meta charset="utf-8">
<title>Terravera Letterhead</title>
<link href="https://fonts.googleapis.com/css2?family=Montserrat:wght@500;700&family=Quicksand:wght@500&display=swap" rel="stylesheet">
<style>
  :root {
    --orange-start: #e2b034;
    --orange-end: #db7f2b;
    --blue-dark: #4686ab;
    --blue-light: #5aa9d1;
    --blue-edge: #3f7ea3;
    --green-light: #68aa4e;
    --green-dark: #579a4d;
    --navy: #3a3f5c;
    --accent: #85cae6;
    --paper: #ffffff;
  }
  html, body {
    margin: 0;
    padding: 0;
    overflow: hidden;
    background: var(--paper);
  }
  .letterhead {
    position: relative;
    width: 849px;
    height: 1200px;
    overflow: hidden;
    background: var(--paper);
  }
  .bands {
    position: absolute;
    inset: 0;
  }
  .brand {
    position: absolute;
    left: 53px;
    top: 96px;
    display: flex;
    align-items: center;
    gap: 10px;
  }
  .brand-dot {
    width: 62px;
    height: 62px;
    border-radius: 50%;
    background: var(--accent);
  }
  .brand-text {
    padding-top: 6px;
  }
  .brand-name {
    font-family: "Montserrat", sans-serif;
    font-weight: 700;
    font-size: 23px;
    letter-spacing: 4.5px;
    color: var(--navy);
    line-height: 1;
    margin: 0;
  }
  .brand-tagline {
    font-family: "Montserrat", sans-serif;
    font-weight: 500;
    font-size: 10.5px;
    color: var(--navy);
    margin: 3px 0 0;
    white-space: nowrap;
  }
  .contact {
    position: absolute;
    left: 619px;
    top: 1041px;
    margin: 0;
    padding: 0;
    list-style: none;
    font-family: "Quicksand", sans-serif;
    font-weight: 500;
    font-size: 13px;
    color: var(--paper);
  }
  .contact li {
    display: flex;
    align-items: center;
    height: 21.5px;
    white-space: nowrap;
  }
  .contact-icon {
    width: 18px;
    height: 16px;
    margin-right: 8px;
    flex: none;
  }
</style>
</head>
<body>
<div class="letterhead">
  <svg class="bands" width="849" height="1200" viewBox="0 0 849 1200">
    <defs>
      <linearGradient id="topBand" x1="0" y1="0" x2="1" y2="0">
        <stop offset="0" stop-color="var(--orange-start)"/>
        <stop offset="1" stop-color="var(--orange-end)"/>
      </linearGradient>
      <linearGradient id="blueBand" x1="0" y1="0" x2="1" y2="1">
        <stop offset="0" stop-color="var(--blue-dark)"/>
        <stop offset="1" stop-color="var(--blue-light)"/>
      </linearGradient>
      <linearGradient id="greenBand" x1="0" y1="0" x2="0" y2="1">
        <stop offset="0" stop-color="var(--green-light)"/>
        <stop offset="1" stop-color="var(--green-dark)"/>
      </linearGradient>
    </defs>
    <path class="band-top" d="M0 0 H849 V94 Q440 -60 0 105 Z" fill="url(#topBand)"/>
    <path class="band-blue-edge" d="M0 727 Q200 1070 541 1200 H0 Z" fill="var(--blue-edge)"/>
    <path class="band-blue" d="M0 742 Q196 1080 520 1200 H0 Z" fill="url(#blueBand)"/>
    <path class="band-green" d="M849 742 Q720 980 523 1103 Q680 1165 849 1181 Z" fill="url(#greenBand)"/>
  </svg>

  <header class="brand">
    <div class="brand-dot"></div>
    <div class="brand-text">
      <h1 class="brand-name">TERRAVERA</h1>
      <p class="brand-tagline">Turning evidence into better choices</p>
    </div>
  </header>

  <ul class="contact">
    <li>
      <svg class="contact-icon" viewBox="0 0 18 16"><path d="M9 1a5 5 0 0 0-5 5c0 3.5 5 9 5 9s5-5.5 5-9a5 5 0 0 0-5-5zm0 7a2 2 0 1 1 0-4 2 2 0 0 1 0 4z" fill="#fff"/></svg>
      Terravera Address
    </li>
    <li>
      <svg class="contact-icon" viewBox="0 0 18 16"><rect x="5.5" y="1" width="7" height="14" rx="1.2" fill="none" stroke="#fff" stroke-width="1.4"/><circle cx="9" cy="12.8" r="0.8" fill="#fff"/></svg>
      +999 999 999
    </li>
    <li>
      <svg class="contact-icon" viewBox="0 0 18 16"><rect x="2" y="3.5" width="14" height="9" fill="#fff"/><path d="M2 3.5 L9 9 L16 3.5" fill="none" stroke="var(--green-dark)" stroke-width="1.2"/></svg>
      hello@terravera-mail.com
    </li>
    <li>
      <svg class="contact-icon" viewBox="0 0 18 16"><circle cx="9" cy="8" r="5" fill="#fff"/></svg>
      social.example/terravera
    </li>
  </ul>
</div>
</body>
</html>
```